Conference website: Kestrel Meridian Forum 2015

We need a web design to help develop a modern and interactive website for the 2nd Kestrel Meridian Summit which main objective will be to present and discuss real-life KmR business initiatives being implemented by entrepreneurs and corporate innovators that are driving sustainable innovation from the bottom up

This is a bi-annual event and will build on the 1st Kestrel Meridian Forum
http://www.kestrelmeridian.org/summit-2013. It is important that the new website maintain consistency with the 1) the Kestrel Meridian Logo (www.kestrelmeridian.org), 2) the visual identity from the fist event and 3) the organization TLQ Logo (www.t7lq.org) -- but the design should be modern, clean, and crisp.

Target Market(s)

Corporations, academics, executives, entrepreneurs, consultants, multilateral organizations, founders, institutions

Industry/Entity Type

Business

Coding

Coded - Design and coding required

Number of Pages Required

5+ page

Font styles to use
Sans Serif

Colors
f68d4d
9bcb3b
3276b5
faa54b
00a88f
0792cd
f37022
9bcb3c
0355a3

Requirements
Must have
• maintain consistency with Kestrel Meridian Logo
• dynamic to get the attention
• design modern, clean and crisp
• content should be well linked (e.i. photos and bios liked to the name of speaker on sessions).
• Has to link to a registration system
• Needs to be under the Kestrel Meridian domain www.kestrelmeridian.org
• Preference to URL kestrelmeridian.org/Summit2015
Nice to have
• different techniques to display menus, photos and bios and description of sessions
• connect somehow with the visual communication developed on last summit in 2013
Should not have
• should not be the same previously
• should not be traditional
• should not be static

```html
<!DOCTYPE html>
<html lang="en">
<head>
<meta charset="utf-8">
<title>Kestrel Meridian Forum 2015</title>
<link rel="stylesheet" href="https://fonts.googleapis.com/css2?family=Open+Sans:wght@400;600;700&family=Oswald:wght@600&display=swap">
<style>
:root{
  --navy:#0b3a78;
  --navy-deep:#0a3270;
  --title-blue:#1d3f8e;
  --green:#7cb53a;
  --orange:#e8762f;
  --rust:#c1582b;
  --text:#555;
  --muted:#888;
  --footer-bg:#ececec;
  --line:#d6d6d6;
  --white:#fff;
}
*{box-sizing:border-box;margin:0;padding:0}
html,body{width:1200px;height:2187px;overflow:hidden}
body{position:relative;background:var(--white);font-family:"Open Sans",Arial,sans-serif;color:var(--text)}
.abs{position:absolute}
.top-rule{left:0;top:0;width:1200px;height:7px;background:var(--navy)}
/* header */
.brand{left:84px;top:26px;width:180px;text-align:center}
.brand-mark{display:block;margin:0 auto 8px;width:82px;height:82px;border-radius:50%;background:var(--navy)}
.brand-name{font-size:19px;font-weight:600;color:var(--navy);line-height:1.1;white-space:nowrap}
.event-date{left:430px;top:24px;width:240px;text-align:right;line-height:1.2}
.event-date strong{display:block;font-size:21px;font-weight:600;color:var(--navy)}
.event-date span{font-size:18px;color:var(--orange)}
.countdown{left:697px;top:31px;width:236px;height:35px;border:1px solid var(--line);border-radius:3px;display:flex;justify-content:space-around;align-items:center;padding:0 6px}
.countdown b{display:block;width:36px;height:25px;background:linear-gradient(#fafafa,#cfcfcf);border:1px solid #999;font:700 17px/23px "Open Sans",sans-serif;color:#222;text-align:center}
.btn-register{left:958px;top:31px;width:143px;height:36px;background:var(--green);color:var(--white);font-size:14px;font-weight:600;display:flex;align-items:center;justify-content:center;gap:8px;border-radius:2px}
.skyline{left:770px;top:100px;width:324px;height:46px;background:linear-gradient(90deg,rgba(220,220,220,0),#e2e2e2 30%,#d4d4d4)}
.main-nav{left:297px;top:147px;width:804px;height:44px;background:var(--navy);display:flex;list-style:none}
.main-nav li{font-size:12.5px;font-weight:600;color:var(--white);line-height:44px;padding:0 14px;white-space:nowrap}
.main-nav li.is-active{background:var(--green);padding:0 18px}
/* hero */
.hero{left:0;top:191px;width:1200px;height:553px;background:
  radial-gradient(ellipse 260px 70px at 180px 120px,rgba(255,255,255,.85),rgba(255,255,255,0)),
  radial-gradient(ellipse 220px 60px at 620px 260px,rgba(255,255,255,.8),rgba(255,255,255,0)),
  radial-gradient(ellipse 180px 50px at 1080px 110px,rgba(255,255,255,.7),rgba(255,255,255,0)),
  radial-gradient(ellipse 140px 260px at 880px 300px,rgba(40,40,50,.55),rgba(40,40,50,0)),
  radial-gradient(ellipse 380px 120px at 300px 520px,rgba(214,190,140,.9),rgba(214,190,140,0)),
  linear-gradient(180deg,#2f72c4 0%,#6fa6e0 22%,#b8d3ee 36%,#6f8a3a 46%,#55702a 58%,#8a6b3c 74%,#a98a58 90%,#c2a474 100%)}
.hero-title{left:99px;top:318px;font-family:"Oswald",sans-serif;font-weight:600;font-size:52px;color:var(--white);letter-spacing:.5px;text-shadow:2px 3px 4px rgba(0,0,0,.5)}
.hero-arrow{top:413px;width:34px;height:41px;background:rgba(20,20,20,.75);display:flex;align-items:center;justify-content:center}
/* welcome */
.welcome{left:99px;top:671px;width:1002px;height:175px;background:var(--white);border:1px solid #e2e2e2;box-shadow:0 2px 6px rgba(0,0,0,.08);text-align:center;padding:30px 118px 0}
.welcome h1{font-size:27px;font-weight:600;color:var(--title-blue);margin-bottom:10px}
.welcome p{font-size:13px;line-height:1.65;color:var(--muted)}
/* feature cards */
.card{top:884px;width:223px;height:291px;color:var(--white);text-align:center}
.card-photo{height:136px}
.card h2{font-size:17px;font-weight:600;margin:17px 0 12px}
.card p{font-size:10.5px;line-height:1.45;padding:0 10px;opacity:.85}
.card .more{display:inline-block;margin-top:12px;background:var(--white);color:#333;font-size:10px;font-weight:700;padding:3px 8px}
.card--blue{left:99px;background:linear-gradient(#2d56a8,#1b2f78)}
.card--green{left:359px;background:linear-gradient(#78b234,#5c9a24)}
.card--rust{left:617px;background:linear-gradient(#d06a31,#b04a22)}
.card--grey{left:876px;background:linear-gradient(#505050,#2e2e2e)}
.photo-stage{background:radial-gradient(ellipse 90px 50px at 150px 40px,rgba(240,120,60,.9),rgba(240,120,60,0)),radial-gradient(ellipse 70px 70px at 70px 90px,rgba(20,30,70,.9),rgba(20,30,70,0)),linear-gradient(160deg,#3a4a9a,#8a3a4a 55%,#1e2250)}
.photo-mic{background:radial-gradient(ellipse 80px 40px at 110px 100px,rgba(230,200,180,.8),rgba(230,200,180,0)),linear-gradient(170deg,#e9eff6,#b9cbe0 50%,#7f9cc0)}
.photo-pen{background:radial-gradient(ellipse 70px 50px at 150px 70px,rgba(160,110,90,.7),rgba(160,110,90,0)),linear-gradient(180deg,#f1e4da,#d6b9a6 60%,#b48a72)}
.photo-hands{background:radial-gradient(ellipse 90px 40px at 110px 70px,rgba(200,150,120,.85),rgba(200,150,120,0)),linear-gradient(180deg,#c9c1b6,#8e8176 60%,#5d6470)}
/* about */
.about{left:99px;top:1215px;width:1002px;height:132px;background:var(--white);border:1px solid #e2e2e2;box-shadow:0 14px 16px -10px rgba(0,0,0,.35);padding:26px 27px}
.about h2{font-size:27px;font-weight:400;color:var(--title-blue);margin-bottom:8px}
.about p{width:710px;font-size:11.5px;line-height:1.65;color:#333}
.about p a{color:var(--rust);text-decoration:none;font-size:11px}
.btn-about{left:878px;top:1258px;width:202px;height:44px;background:var(--navy);color:var(--white);font-size:18px;display:flex;align-items:center;justify-content:center;gap:12px;border-radius:3px}
/* sponsors */
.section-label{left:0;width:1200px;text-align:center;font-size:12px;color:var(--muted)}
.logo-row{left:99px;width:1002px;display:flex;justify-content:center;align-items:center}
.logo-name{font-weight:700;color:#333;white-space:nowrap}
.sponsors .logo-name{font-size:28px;color:var(--navy)}
.partners .logo-name{font-size:18px;color:#555;font-weight:600}
.divider{left:99px;top:1602px;width:1000px;height:1px;background:var(--line)}
/* footer */
.footer{left:0;top:1885px;width:1200px;height:223px;background:var(--footer-bg)}
.f-col{top:1922px}
.f-col h3{font-size:13px;font-weight:600;color:var(--navy);margin-bottom:18px}
.f-sep{top:1920px;width:1px;height:150px;background:var(--line)}
.org{display:flex;align-items:center;gap:8px;width:160px;font-size:14px;font-weight:600;color:#444;line-height:1.15;margin-bottom:20px}
.org i{flex:none;display:block;width:30px;height:30px;border-radius:50%;background:var(--green)}
.org i.sq{border-radius:0;background:#2f5a2c;height:42px}
.contact{font-size:11px;line-height:1.6;color:#8a8a8a}
.contact .row{display:flex;gap:8px;margin-bottom:10px}
.contact svg{flex:none;margin-top:3px}
.quick{list-style:none;font-size:8px;text-transform:uppercase;color:#8a8a8a;line-height:17px}
.email-field{display:flex;width:155px;height:26px;margin-bottom:20px}
.email-field span{flex:1;background:var(--white);font-size:10px;color:#777;padding:6px 8px}
.email-field b{width:34px;background:#c8c8c8;display:flex;align-items:center;justify-content:center}
.social{display:flex;gap:12px}
.social i{display:block;width:25px;height:25px;border-radius:50%}
.bottom-bar{left:0;top:2108px;width:1200px;height:79px;background:var(--navy-deep)}
.copyright{left:99px;top:2139px;font-size:12px;color:var(--white)}
.to-top{left:1075px;top:2135px;width:24px;height:24px;border:2px solid #8aa6d0;border-radius:50%;display:flex;align-items:center;justify-content:center}
</style>
</head>
<body>
<div class="abs top-rule"></div>

<header>
  <div class="abs brand"><span class="brand-mark"></span><div class="brand-name">Kestrel Meridian</div></div>
  <div class="abs event-date"><strong>July 16 and 17, 2015</strong><span>Cedarport, Vermont</span></div>
  <div class="abs countdown"><b>01</b><b>06</b><b>21</b><b>02</b><b>30</b></div>
  <div class="abs btn-register">
    <svg width="14" height="14" viewBox="0 0 14 14"><rect x="1" y="3" width="10" height="10" fill="none" stroke="#fff" stroke-width="1.6"/><path d="M6 8l7-7" stroke="#fff" stroke-width="2"/></svg>
    Register Now</div>
  <div class="abs skyline" role="img" aria-label="Line illustration of industry, farming, water, city and transport icons"></div>
  <ul class="abs main-nav">
    <li class="is-active">HOME</li><li>KESTREL MERIDIAN</li><li>KNOWLEDGE BASE</li><li>SPONSORS &amp; PARTNERS</li><li>JOIN US</li><li>EVENTS</li><li>CONTACTUS</li>
  </ul>
</header>

<section>
  <div class="abs hero" role="img" aria-label="Photo of farm workers harvesting grain on a hillside under a blue sky with white clouds"></div>
  <div class="abs hero-title">PROVOKE. DISCUSS. ACT</div>
  <div class="abs hero-arrow" style="left:0"><svg width="12" height="22"><path d="M10 1L2 11l8 10" fill="none" stroke="#fff" stroke-width="1.5"/></svg></div>
  <div class="abs hero-arrow" style="left:1166px"><svg width="12" height="22"><path d="M2 1l8 10-8 10" fill="none" stroke="#fff" stroke-width="1.5"/></svg></div>
  <div class="abs welcome">
    <h1>Welcome to 2nd Kestrel Meridian Forum 2015</h1>
    <p>The Base of the Pyramid (KmR) is a socio-economic designation for the more than 4 billion people living on less than $8 a day. It is also a business strategy that focuses on products, services and enterprises to serve this demographic in a way that is culturally sensitive, environmentally sustainable and economically profitable.</p>
  </div>
</section>

<section>
  <div class="abs card card--blue"><div class="card-photo photo-stage" role="img" aria-label="Photo of a speaker at a lit conference stage"></div><h2>Speakers &amp; Contributors</h2><p>Etiam vel massa elementum, bibendum tellus venenatis, feugiat massa. Curabi tur venenatis lacinia ornare.</p><span class="more">MORE</span></div>
  <div class="abs card card--green"><div class="card-photo photo-mic" role="img" aria-label="Photo of a conference microphone"></div><h2>Summit Schedule</h2><p>Etiam vel massa elementum, bibendum tellus venenatis, feugiat massa. Curabi tur venenatis lacinia ornare.</p><span class="more">MORE</span></div>
  <div class="abs card card--rust"><div class="card-photo photo-pen" role="img" aria-label="Photo of a hand writing with a pen"></div><h2>Program Descriptions</h2><p>Etiam vel massa elementum, bibendum tellus venenatis, feugiat massa. Curabi tur venenatis lacinia ornare.</p><span class="more">MORE</span></div>
  <div class="abs card card--grey"><div class="card-photo photo-hands" role="img" aria-label="Photo of joined hands in a team huddle"></div><h2>How to Sponsor</h2><p>Etiam vel massa elementum, bibendum tellus venenatis, feugiat massa. Curabi tur venenatis lacinia ornare.</p><span class="more">MORE</span></div>
</section>

<section>
  <div class="abs about">
    <h2>About the Summit</h2>
    <p>sce vitae lectus sit amet mi pulvinar maximus. Aenean placerat, nibh vel accumsan aliquet, magna nibh accumsan nibh, ac tempus nunc ipsum ac tellus. Cras augue magna, placerat eget nulla non, congue suscipit neque. &nbsp;<a>READ MORE</a></p>
  </div>
  <div class="abs btn-about">REISTER NOW
    <svg width="26" height="26"><circle cx="13" cy="13" r="11" fill="none" stroke="#fff" stroke-width="1.5"/><path d="M11 8l5 5-5 5" fill="none" stroke="#fff" stroke-width="1.5"/></svg></div>
</section>

<section class="sponsors">
  <div class="abs section-label" style="top:1418px">Diamond Sponsors</div>
  <div class="abs logo-row" style="top:1485px;gap:56px">
    <span class="logo-name">Arvend Copperline</span><span class="logo-name">Pallidor Foods</span><span class="logo-name">Ostrava</span><span class="logo-name">Vellmar</span>
  </div>
</section>
<div class="abs divider"></div>
<section class="partners">
  <div class="abs section-label" style="top:1642px">Partners and Collaborators</div>
  <div class="abs logo-row" style="top:1700px;gap:70px">
    <span class="logo-name">Harrowgate</span><span class="logo-name">gcbpn</span><span class="logo-name">Morrell</span><span class="logo-name">Wendholt University</span>
  </div>
  <div class="abs logo-row" style="top:1790px;gap:56px">
    <span class="logo-name">Corwin Ashby Institute</span><span class="logo-name">Halvern Enterprise Center</span><span class="logo-name">Acorn Pledge</span><span class="logo-name">Fieldgrain Lab</span><span class="logo-name">BRISK</span>
  </div>
</section>

<footer>
  <div class="abs footer"></div>
  <div class="abs f-col" style="left:99px">
    <h3>ORGANIZERS</h3>
    <div class="org"><i></i>TLQ</div>
    <div class="org"><i class="sq"></i>Northgate<br>University</div>
  </div>
  <div class="abs f-sep" style="left:274px"></div>
  <div class="abs f-col contact" style="left:313px;width:220px">
    <h3>CONTACT US</h3>
    <div class="row"><svg width="8" height="11"><path d="M4 11C1 6 0 5 0 4a4 4 0 018 0c0 1-1 2-4 7z" fill="#aaa"/></svg><div>Conference Content Questions<br>55 Building name, Street name<br>City - Zipcode</div></div>
    <div class="row"><svg width="10" height="10"><path d="M2 0l2 3-1 1c1 2 2 3 3 3l1-1 3 2-2 2C4 10 0 6 0 2z" fill="#aaa"/></svg>Phone: (555) 014-2287</div>
    <div class="row"><svg width="11" height="8"><rect width="11" height="8" fill="#aaa"/><path d="M0 0l5.5 4L11 0" fill="none" stroke="#eee"/></svg>m.rowan@t7lq.org</div>
  </div>
  <div class="abs f-col contact" style="left:547px;width:210px;top:1957px">
    <div class="row"><svg width="8" height="11"><path d="M4 11C1 6 0 5 0 4a4 4 0 018 0c0 1-1 2-4 7z" fill="#aaa"/></svg><div>Registration Questions<br>55 Building name, Street name<br>City - Zipcode</div></div>
    <div class="row"><svg width="10" height="10"><path d="M2 0l2 3-1 1c1 2 2 3 3 3l1-1 3 2-2 2C4 10 0 6 0 2z" fill="#aaa"/></svg>Phone: (555) 019-4410</div>
    <div class="row"><svg width="11" height="8"><rect width="11" height="8" fill="#aaa"/><path d="M0 0l5.5 4L11 0" fill="none" stroke="#eee"/></svg>register@northgate.edu</div>
  </div>
  <div class="abs f-sep" style="left:765px"></div>
  <div class="abs f-col" style="left:787px">
    <h3>QUICK LINKS</h3>
    <ul class="quick"><li>• Home</li><li>• Kestrel Meridian</li><li>• Knowledge Base</li><li>• Sponsors &amp; Partners</li><li>• Join Us</li><li>• Events</li><li>• Contactus</li></ul>
  </div>
  <div class="abs f-sep" style="left:918px"></div>
  <div class="abs f-col" style="left:945px">
    <h3>KEEP ME POSTED</h3>
    <div class="email-field"><span>E-mail</span><b><svg width="9" height="11"><path d="M0 0l9 5.5L0 11z" fill="#666"/></svg></b></div>
    <h3 style="margin-bottom:12px">FOLLOW US ON</h3>
    <div class="social"><i style="background:#2d4f8f"></i><i style="background:#2aa3e0"></i><i style="background:#1d6fa8"></i><i style="background:#f08a24"></i></div>
  </div>
  <div class="abs bottom-bar"></div>
  <div class="abs copyright">Copyright &nbsp;©&nbsp; 2015 &nbsp;Kestrel Meridian Summit 2015. &nbsp;All rights reserved.</div>
  <div class="abs to-top"><svg width="10" height="7"><path d="M0 7l5-7 5 7z" fill="#8aa6d0"/></svg></div>
</footer>
</body>
</html>
```